BrookVale Collision Repair Web Site

Create a web site that will inform my potential customers about the services I provide. We are a Automotive Collision repair business that uses the latest state of the art equipment, computerized paint matching highly trained technicians, have over 30 years experience. We work with all all insurance programs. Our Moto is "Fixed Right, The First Time, Every Time". BrookVale, The trusted pick in collision repair.

Target Market(s)

People that have been in a auto collision, needs windshield replaced, people that drive 10 year or newer cars

Industry/Entity Type

Automotive

Coding

Coded - Design and coding required

Number of Pages Required

4 page

Font styles to use
Sans Serif

Requirements
Must have
• Logo, Place for Phone number, I need to be able to put the code in so I can use a tracking phone number
• site needs to be mobile ready or adaptive
• May want to have a photo of a high end car
• here is a web site for example with the pages that I want
• https://www.pondlyautobody.example/online-repair-estimate,
• https://www.pondlyautobody.example/schedule-appointment
• https://www.pondlyautobody.example/collision-repair/auto-body-repair
• https://www.pondlyautobody.example/contact
Nice to have
• Be great if the Car in the log could have the front damaged then have it fix in a animation. Not sure if could be done here

```html
<!DOCTYPE html>
<html lang="en">
<head>
<meta charset="utf-8">
<title>BrookVale Collision Repair</title>
<link href="https://fonts.googleapis.com/css2?family=Cinzel:wght@400&family=Open+Sans:wght@400;600&family=Raleway:wght@400;500&display=swap" rel="stylesheet">
<style>
:root{
  --blue:#0f4fa3;
  --blue-deep:#0c3f86;
  --blue-bar:#0a3979;
  --green:#65c32f;
  --lime:#7dc242;
  --ink:#333;
  --muted:#666;
  --line:#dcdcdc;
  --white:#fff;
}
*{margin:0;padding:0;box-sizing:border-box}
html,body{width:689px;height:1200px;overflow:hidden;background:var(--white)}
body{position:relative;font-family:"Open Sans",Arial,sans-serif;color:var(--ink)}
.site-header{position:absolute;left:0;top:0;width:689px;height:69px}
.brand{position:absolute;left:68px;top:18px;color:var(--blue);font-family:"Raleway",Arial,sans-serif;font-weight:500;line-height:1}
.brand-name{font-size:22px;letter-spacing:.5px}
.brand-sub{font-size:9.5px;letter-spacing:1.3px;text-transform:uppercase;margin-top:4px}
.call{position:absolute;right:73px;top:28px;text-align:right;font-family:"Raleway",Arial,sans-serif}
.call-label{font-size:10px;color:#888}
.call-number{display:flex;align-items:center;gap:5px;font-size:13px;color:#444;margin-top:2px}
.call-icon{width:15px;height:15px;border-radius:50%;background:var(--lime);display:flex;align-items:center;justify-content:center}
.main-nav{position:absolute;left:0;top:69px;width:689px;height:29px;background:var(--blue)}
.main-nav ul{list-style:none;display:flex;margin-left:63px;height:100%}
.main-nav li{height:100%;display:flex;align-items:center;padding:0 10.5px;font-size:8.6px;color:var(--white);border-right:1px solid rgba(255,255,255,.25);font-family:"Raleway",Arial,sans-serif;font-weight:500}
.main-nav li.active{background:var(--lime);padding:0 17px}
.hero{position:absolute;left:0;top:98px;width:689px;height:254px}
.hero svg{display:block}
.hero-copy{position:absolute;left:79px;top:78px;color:var(--white);font-family:"Raleway",Arial,sans-serif}
.hero-title{font-size:21px;font-weight:400;line-height:25px}
.hero-tag{font-size:12.5px;margin-top:5px}
.hero-dots{display:flex;gap:3px;margin-top:10px}
.hero-dots span{width:11px;height:11px;border-radius:50%;background:var(--white)}
.hero-dots span.on{background:#c8b22c;border:2px solid var(--white)}
.welcome{position:absolute;left:0;top:376px;width:689px;text-align:center}
.welcome h1{font-family:"Cinzel",Georgia,serif;font-weight:400;font-size:22px;color:var(--blue);letter-spacing:1px}
.welcome p{width:490px;margin:10px auto 0;font-size:7.2px;line-height:12px;color:var(--muted)}
.features{position:absolute;left:0;top:473px;width:689px}
.feature{position:absolute;width:170px;text-align:center}
.feature-icon{width:70px;height:70px;margin:0 auto;border-radius:50%;border:2px solid #e3e3e3;background:var(--white);display:flex;align-items:center;justify-content:center}
.feature h2{font-family:"Raleway",Arial,sans-serif;font-weight:400;font-size:11.5px;margin-top:10px;color:#333}
.feature p{font-size:6.6px;line-height:11px;color:var(--muted);margin-top:5px}
.btn{display:inline-block;border:1.5px solid var(--blue);color:var(--blue);font-size:7.2px;padding:5px 11px;margin-top:13px;font-weight:600;font-family:"Raleway",Arial,sans-serif}
.repair-band{position:absolute;left:0;top:674px;width:689px;height:182px;display:flex}
.repair-copy{width:349px;background:var(--green);color:var(--white);text-align:center;padding-top:51px}
.repair-copy h2{font-family:"Raleway",Arial,sans-serif;font-weight:400;font-size:15px}
.repair-copy p{width:230px;margin:8px auto 0;font-size:7.4px;line-height:11px}
.repair-copy .btn{border-color:var(--white);color:var(--white);margin-top:13px;padding:5px 14px}
.repair-photo{flex:1;background:linear-gradient(135deg,#8a8f96 0%,#cfd3d8 35%,#1f3f7a 60%,#3a4250 100%)}
.offers{position:absolute;left:0;top:880px;width:689px}
.offer{position:absolute;display:flex;gap:8px}
.offer-media{width:86px;height:86px;border-radius:50%;flex:none}
.offer h3{font-family:"Raleway",Arial,sans-serif;font-weight:400;font-size:12.5px;color:#333;margin-top:3px}
.offer p{font-size:6.2px;line-height:12px;color:var(--muted);width:185px;margin-top:4px}
.site-footer{position:absolute;left:0;top:1018px;width:689px;height:144px;background:var(--blue-deep);color:var(--white)}
.footer-col{position:absolute;top:30px}
.footer-col h4{font-family:"Raleway",Arial,sans-serif;font-weight:500;font-size:10.5px;text-transform:uppercase;margin-bottom:6px}
.footer-col ul{list-style:none}
.footer-col li{font-size:7.2px;line-height:14.4px;color:#dce6f5;display:flex;align-items:center;gap:4px}
.legal{position:absolute;left:0;top:1162px;width:689px;height:38px;background:var(--blue-bar);font-size:7.2px;color:#c9d6ea;padding:16px 0 0 82px}
</style>
</head>
<body>

<header class="site-header">
  <div class="brand">
    <div class="brand-name">BrookVale</div>
    <div class="brand-sub">Collision Repair</div>
  </div>
  <div class="call">
    <div class="call-label">Call Us Now</div>
    <div class="call-number">
      <span class="call-icon"><svg width="9" height="9" viewBox="0 0 24 24"><path fill="#fff" d="M6.6 10.8a15.1 15.1 0 0 0 6.6 6.6l2.2-2.2c.3-.3.7-.4 1-.2 1.1.4 2.3.6 3.6.6.6 0 1 .4 1 1V20c0 .6-.4 1-1 1A17 17 0 0 1 3 4c0-.6.4-1 1-1h3.5c.6 0 1 .4 1 1 0 1.3.2 2.5.6 3.6.1.3 0 .7-.2 1z"/></svg></span>
      555.310.4821
    </div>
  </div>
</header>

<nav class="main-nav">
  <ul>
    <li class="active">HOME</li>
    <li>ABOUT US</li>
    <li>SERVICES</li>
    <li>TECHNOLOGY</li>
    <li>E QUIPMENTS</li>
    <li>RESOURCES</li>
    <li>NEWS</li>
    <li style="border-right:0">CONTACT</li>
  </ul>
</nav>

<section class="hero">
  <svg width="689" height="254" viewBox="0 0 689 254" role="img" aria-label="Repair shop interior with a damaged blue car and a polishing pad on a blue panel">
    <defs>
      <linearGradient id="shop" x1="0" y1="0" x2="1" y2="1">
        <stop offset="0" stop-color="#9a9c9e"/><stop offset=".6" stop-color="#6d7073"/><stop offset="1" stop-color="#4b4e52"/>
      </linearGradient>
      <linearGradient id="crash" x1="0" y1="0" x2="1" y2="1">
        <stop offset="0" stop-color="#2a4fa8"/><stop offset=".5" stop-color="#8fa6d8"/><stop offset="1" stop-color="#1a2f6e"/>
      </linearGradient>
      <linearGradient id="polish" x1="0" y1="0" x2="1" y2="1">
        <stop offset="0" stop-color="#3c5fae"/><stop offset=".5" stop-color="#cdbf9a"/><stop offset="1" stop-color="#2f4c8e"/>
      </linearGradient>
    </defs>
    <rect width="689" height="254" fill="url(#shop)"/>
    <polygon points="395,0 525,0 435,254 300,254" fill="url(#crash)"/>
    <polygon points="530,0 665,0 575,254 440,254" fill="url(#polish)"/>
    <polygon points="525,0 530,0 440,254 435,254" fill="#fff"/>
  </svg>
  <div class="hero-copy">
    <div class="hero-title">Fix Right, the first time,<br>every time, &amp; BrookVale,</div>
    <div class="hero-tag">The trusted pick in collision repair</div>
    <div class="hero-dots"><span class="on"></span><span></span><span></span><span></span></div>
  </div>
</section>

<section class="welcome">
  <h1>WELCOME TO BROOKVALE</h1>
  <p>Maecenas aliquet velit vel turpis Mauris neque metus malesuada nec ultricies sit amet porttitor mattis enim In massa libero interdum nec interdum vel blandit sed nulla In ullamcorper est eget tempor cursus neque mi consectetuer mi a ultricies massa est sed nisl Class aptent taciti sociosqu ad litora torquent per conubia nostra per inceptos hymena</p>
</section>

<section class="features">
  <div class="feature" style="left:73px">
    <div class="feature-icon"><svg width="32" height="32" viewBox="0 0 32 32"><path fill="#0f4fa3" d="M4 17l3-6h10l2 6v8h-3v-2H7v2H4z"/><circle cx="8" cy="20" r="1.6" fill="#fff"/><circle cx="16" cy="20" r="1.6" fill="#fff"/><path fill="#0f4fa3" d="M24 3a5 5 0 0 0-3 8v16a2 2 0 0 0 4 0V11a5 5 0 0 0-3-8v4h2z"/></svg></div>
    <h2>Collision Repair</h2>
    <p>Maecenas aliquet velit vel turpis Mauris neque metus malesuada nec ultricies sit amet porttitor mattis enim In massa libero interd</p>
    <span class="btn">READ MORE</span>
  </div>
  <div class="feature" style="left:260px">
    <div class="feature-icon"><svg width="32" height="32" viewBox="0 0 32 32" fill="none" stroke="#0f4fa3" stroke-width="2.6"><rect x="4" y="6" width="14" height="9" rx="4.5" transform="rotate(40 11 10.5)"/><rect x="14" y="16" width="14" height="9" rx="4.5" transform="rotate(40 21 20.5)"/></svg></div>
    <h2>Our Technology</h2>
    <p>Maecenas aliquet velit vel turpis Mauris neque metus malesuada nec ultricies sit amet porttitor mattis enim In massa libero interd</p>
    <span class="btn">READ MORE</span>
  </div>
  <div class="feature" style="left:449px">
    <div class="feature-icon"><svg width="34" height="34" viewBox="0 0 34 34"><circle cx="17" cy="17" r="14" fill="none" stroke="#0f4fa3" stroke-width="3.2"/><circle cx="17" cy="17" r="3" fill="#0f4fa3"/><g stroke="#0f4fa3" stroke-width="3"><line x1="17" y1="5" x2="17" y2="14"/><line x1="17" y1="20" x2="17" y2="29"/><line x1="5" y1="17" x2="14" y2="17"/><line x1="20" y1="17" x2="29" y2="17"/><line x1="8.5" y1="8.5" x2="15" y2="15"/><line x1="19" y1="19" x2="25.5" y2="25.5"/><line x1="25.5" y1="8.5" x2="19" y2="15"/><line x1="15" y1="19" x2="8.5" y2="25.5"/></g></svg></div>
    <h2>Our Equipments</h2>
    <p>Maecenas aliquet velit vel turpis Mauris neque metus malesuada nec ultricies sit amet porttitor mattis enim In massa libero interd</p>
    <span class="btn">READ MORE</span>
  </div>
</section>

<section class="repair-band">
  <div class="repair-copy">
    <h2>How we Reparing</h2>
    <p>Praesent sit amet est In dictum dolor eu dictum porttitor enim felis viverra mi eget luctus massa purus quis odio Etiam nulla massa pharetra facilisis volutpat in imperdiet</p>
    <span class="btn">READ MORE</span>
  </div>
  <div class="repair-photo" role="img" aria-label="Mechanic in blue work uniform repairing a car engine"></div>
</section>

<section class="offers">
  <div class="offer" style="left:73px">
    <div class="offer-media" role="img" aria-label="Polishing machine buffing a red car panel" style="background:radial-gradient(circle at 45% 40%,#3a63c9 0%,#2a4aa0 30%,#d9333b 60%,#f1f1f1 100%)"></div>
    <div>
      <h3>Latest Offers</h3>
      <p>Maecenas aliquet velit vel turpis Mauris neque metus malesuada nec ultricies sit amet porttitor mattis enim In massa libero interdum nec interdum vel blandit sed nulla In ullamcorper est eget tempor cursus neque mi consectetuer mi a ultricies massa est sed nisl</p>
    </div>
  </div>
  <div class="offer" style="left:357px">
    <div class="offer-media" role="img" aria-label="Gold guarantee seal" style="background:radial-gradient(circle,#e9c35a 0%,#b8862a 60%,#7a5614 100%)"></div>
    <div>
      <h3>Lifetime Guarantee</h3>
      <p>Maecenas aliquet velit vel turpis Mauris neque metus malesuada nec ultricies sit amet porttitor mattis enim In massa libero interdum nec interdum vel blandit sed nulla In ullamcorper est eget tempor cursus neque mi consectetuer mi a ultricies massa est sed nisl</p>
    </div>
  </div>
</section>

<footer class="site-footer">
  <div class="footer-col" style="left:86px">
    <h4>Company</h4>
    <ul><li>Home</li><li>About Us</li><li>Browse Location</li><li>Clients</li></ul>
  </div>
  <div class="footer-col" style="left:174px">
    <h4>Services</h4>
    <ul><li>How we work</li><li>Technology</li><li>Equipments</li><li>&nbsp;Auto Glass</li></ul>
  </div>
  <div class="footer-col" style="left:267px">
    <h4>Sublinks</h4>
    <ul><li>Online Auto Glass Quote</li><li>Schedule Appointment</li><li>Windshield Replacement</li><li>Windshield Repair</li><li>Mobile Auto Glass Service</li></ul>
  </div>
  <div class="footer-col" style="left:385px">
    <h4>Repairing</h4>
    <ul><li>Online Collision Estimate</li><li>Schedule Appointment</li><li>Auto Body Repair</li><li>Hail Damage Repair</li><li>Paintless Dent Repair</li></ul>
  </div>
  <div class="footer-col" style="left:513px">
    <h4>Contact Info</h4>
    <ul>
      <li>412 Millbrook Avenue Suite B12</li>
      <li>Fairhollow, PA 19990</li>
      <li style="margin-top:4px"><svg width="8" height="8" viewBox="0 0 24 24"><path fill="#fff" d="M6.6 10.8a15.1 15.1 0 0 0 6.6 6.6l2.2-2.2c.3-.3.7-.4 1-.2 1.1.4 2.3.6 3.6.6.6 0 1 .4 1 1V20c0 .6-.4 1-1 1A17 17 0 0 1 3 4c0-.6.4-1 1-1h3.5c.6 0 1 .4 1 1 0 1.3.2 2.5.6 3.6.1.3 0 .7-.2 1z"/></svg>(555) 204-7730</li>
      <li><svg width="8" height="7" viewBox="0 0 24 18"><rect width="24" height="18" fill="#fff"/><path d="M0 0l12 9 12-9" fill="none" stroke="#0c3f86" stroke-width="2"/></svg>info@brookvalerepair.example</li>
    </ul>
  </div>
</footer>

<div class="legal">© 2016 Company Name&nbsp; All right reserved&nbsp; Term of Use</div>

</body>
</html>
```